Dental lab wants website to get in touch with dentists, dental surgeons, dental students..

We want an overal informative website so people can now who we are, what we do, how to contact us.
We do NOT focus towards patients, but to primarely to dentists,also dental surgeons, dental students, ... (business to business)
We are an innovative company, who work with highly skilled technicians, as well as highly skilled cadcam operators.
CNC milling, 3D printing, CAD design, is all done in house.
Today we lack a tool to communicate that on the internet, hence the website.
for some ideas about our company you can visit www.plivora.com/mertanvik
I also uploaded the logo, the blue color, an flyer we made recently.
Use it as inspiration, but don't just follow that style.
good luck,
Dental
4 page
- homepage, contactpage, who are we, .... When we like the concept, we want to have this website extended and build by the designer. But first we want to have a feel how it can look.

```html
<!DOCTYPE html>
<html lang="en">
<head>
<meta charset="utf-8">
<title>Dentaris Lab</title>
<link href="https://fonts.googleapis.com/css2?family=Open+Sans:wght@300;400;600;700&display=swap" rel="stylesheet">
<style>
:root{
  --teal:#12a89a;
  --teal-dark:#0e8f83;
  --red:#ee2848;
  --ink:#333;
  --muted:#8a8a8a;
  --light:#f2f2f2;
  --line:#e3e3e3;
  --dark:#2d2d2d;
  --white:#fff;
}
*{box-sizing:border-box;margin:0;padding:0}
html,body{width:1200px;height:3764px;overflow:hidden}
body{font-family:"Open Sans",Arial,sans-serif;color:var(--ink);background:var(--white);position:relative}
.wrap{width:900px;margin:0 auto;position:relative}
.btn{display:inline-block;font-size:13px;font-weight:600;letter-spacing:.5px;padding:10px 22px;text-transform:uppercase}
.btn-teal{background:var(--teal);color:var(--white)}
.btn-grey{background:#b5b5b5;color:var(--white)}
.btn-outline{border:1px solid #cfcfcf;color:var(--ink);background:var(--white)}
.media{position:absolute}

/* hero */
.hero{position:relative;height:512px;overflow:hidden}
.hero .media{inset:0;background:linear-gradient(90deg,#e9ecef 0%,#f6f4f2 30%,#cfb8a8 50%,#f3f1ef 70%,#eef0f2 100%)}
.logo{position:absolute;left:160px;top:72px;width:180px;height:80px;background:var(--red);color:var(--white);display:flex;align-items:center;justify-content:center;font-weight:700;font-size:22px}
.hero-caption{position:absolute;left:0;right:0;top:320px;text-align:center}
.hero-caption h1{color:var(--red);font-size:44px;font-weight:700;letter-spacing:1px}
.hero-caption p{font-size:15px;color:var(--dark);letter-spacing:2px;text-transform:uppercase;margin-top:2px}
.dots{position:absolute;right:160px;top:394px;display:flex;gap:10px}
.dots span{width:12px;height:12px;border-radius:50%;background:#777}
.dots span:first-child{background:var(--red)}
.nav{position:absolute;left:150px;top:432px;width:900px;height:80px;background:#e7e7e7;display:flex}
.nav a{display:flex;align-items:center;padding:0 38px;font-size:13px;font-weight:600;color:#777;text-decoration:none;text-transform:uppercase}
.nav a.active{background:var(--teal);color:var(--white)}

/* welcome */
.welcome{background:var(--teal);height:328px;text-align:center;color:var(--white);position:relative}
.welcome h2{font-size:30px;font-weight:700;padding-top:108px}
.welcome p{width:900px;margin:28px auto 0;font-size:15px;line-height:1.7}
.welcome .btn{position:absolute;left:50%;bottom:-20px;transform:translateX(-50%);background:var(--white);color:var(--teal);border:1px solid var(--line)}

/* features */
.features{height:352px;border-bottom:1px solid var(--line)}
.features .wrap{display:flex;gap:60px;padding-top:90px}
.feature{flex:1;display:grid;grid-template-columns:56px 1fr;column-gap:16px}
.feature .icon{width:46px;height:46px;border-radius:50%;background:#cfcfcf;display:flex;align-items:center;justify-content:center}
.feature h3{font-size:14px;font-weight:700;text-transform:uppercase;padding-top:12px}
.feature p{grid-column:2;font-size:13px;line-height:1.6;color:var(--muted);margin:10px 0 18px}
.feature .btn{grid-column:2;justify-self:start;padding:8px 18px}

/* step */
.step{position:relative;height:348px;margin-top:12px}
.step .photo{left:0;top:0;width:760px;height:348px;background:linear-gradient(90deg,#7a2a2e 0%,#c96b6b 45%,#e7c3bd 80%,#eef1f3 100%)}
.step .panel{position:absolute;left:760px;top:0;right:0;height:348px;background:linear-gradient(180deg,#e9eef1,#f7f8f9)}
.step h2{position:absolute;left:768px;top:84px;font-size:50px;font-weight:300;color:var(--teal);line-height:1.1}
.step p{position:absolute;left:770px;top:208px;width:250px;font-size:13px;line-height:1.6;color:var(--muted)}
.to-top{position:absolute;right:66px;top:280px;width:54px;height:54px;border-radius:50%;background:var(--white);display:flex;align-items:center;justify-content:center;box-shadow:0 1px 4px rgba(0,0,0,.15)}

/* news */
.news{height:648px;padding-top:90px}
.news .wrap{display:flex;justify-content:space-between}
.news-list{width:450px}
.section-label{font-size:13px;font-weight:700;text-transform:uppercase;letter-spacing:.5px}
.item{display:grid;grid-template-columns:80px 1fr;column-gap:24px;margin-top:40px}
.item:first-of-type{margin-top:34px}
.date{width:80px;height:80px;border-radius:50%;background:var(--dark);color:var(--white);display:flex;flex-direction:column;align-items:center;justify-content:center;line-height:1}
.date b{font-size:28px}
.date span{font-size:13px;font-weight:700;margin-top:4px}
.item h4{font-size:13px;font-weight:700;text-transform:uppercase;margin-top:6px}
.item p{font-size:13px;line-height:1.6;color:var(--muted);margin-top:6px}
.news-list .btn{margin:30px 0 0 0}
.news-side{width:362px}
.news-side .img{height:176px;position:relative}
.news-side .img-a{background:linear-gradient(135deg,#e9eef0,#cfd9dc 50%,#f2e7e0)}
.news-side .img-b{background:linear-gradient(135deg,#5c9a8e,#c7a792 50%,#efe3da);margin-top:28px}
.news-side h3{font-size:20px;font-weight:700;color:var(--teal);text-transform:uppercase;line-height:1.2;margin-top:14px}

/* smile */
.smile{background:var(--light);height:572px;text-align:center;position:relative}
.smile h2{font-size:24px;font-weight:700;padding-top:78px;text-transform:uppercase}
.smile h2 em{font-style:normal;color:var(--teal)}
.smile .img{position:absolute;left:384px;top:140px;width:432px;height:192px;background:linear-gradient(180deg,#e6c8b8,#f4ece6 55%,#d9b0a2)}
.arrow{position:absolute;top:220px;color:#bbb}
.smile p{position:absolute;left:150px;top:372px;width:900px;font-size:14px;line-height:1.7;color:var(--muted)}
.smile .btn{position:absolute;left:50%;top:482px;transform:translateX(-50%)}

/* advantages */
.advantages{height:392px;padding-top:60px}
.advantages .section-label{padding-bottom:20px;border-bottom:1px solid var(--line)}
.cols{display:flex;gap:60px;margin-top:44px}
.col{flex:1}
.col h3{font-size:22px;font-weight:600}
.col p{font-size:13px;line-height:1.6;color:var(--muted);margin:14px 0 24px}
.col .btn{padding:8px 18px;font-size:12px}

/* banner */
.banner{position:relative;height:428px}
.banner .photo{inset:0;background:linear-gradient(90deg,#6d4d46 0%,#c9a396 40%,#e8ddd6 70%,#d6d9db 100%)}
.banner .card{position:absolute;left:460px;top:128px;width:588px;height:300px;background:var(--red);color:var(--white);padding:48px 60px}
.banner .card h2{font-size:44px;font-weight:300;line-height:1.2;width:360px}
.banner .go{position:absolute;right:58px;top:118px;width:80px;height:80px;border-radius:50%;background:var(--white);display:flex;align-items:center;justify-content:center}

/* footer */
.footer{background:var(--teal);height:104px;color:var(--white)}
.footer .wrap{height:104px;display:flex;align-items:center}
.footer small{font-size:13px;font-weight:600}
.social{position:absolute;left:50%;transform:translateX(-50%);display:flex;gap:14px}
.social span{width:34px;height:34px;border-radius:50%;border:1px solid rgba(255,255,255,.6)}
</style>
</head>
<body>

<header class="hero">
  <div class="media" role="img" aria-label="Smiling woman holding a dental mirror on a light background"></div>
  <div class="logo">Dentaris Lab</div>
  <div class="hero-caption">
    <h1>DIAMONDS</h1>
    <p>Smiles crafted forever</p>
  </div>
  <div class="dots"><span></span><span></span><span></span></div>
  <nav class="nav">
    <a class="active">About us</a><a>Services</a><a>News</a><a>Our work</a><a>Contacts</a>
  </nav>
</header>

<section class="welcome">
  <h2>Welcome to our website!</h2>
  <p>Our laboratory partners with dentists, surgeons and students across the region. Skilled technicians and CAD/CAM operators handle design, CNC milling and 3D printing in house, delivering precise restorations on time, every time, with clear communication.</p>
  <span class="btn">More</span>
</section>

<section class="features">
  <div class="wrap">
    <div class="feature">
      <div class="icon"><svg width="20" height="20" viewBox="0 0 20 20"><circle cx="10" cy="10" r="6" fill="none" stroke="#fff" stroke-width="2"/></svg></div>
      <h3>Precise digital design</h3>
      <p>Every case is modelled by trained CAD operators and checked twice before production starts.</p>
      <span class="btn btn-grey">More</span>
    </div>
    <div class="feature">
      <div class="icon"><svg width="20" height="20" viewBox="0 0 20 20"><rect x="4" y="4" width="12" height="12" fill="none" stroke="#fff" stroke-width="2"/></svg></div>
      <h3>In house milling</h3>
      <p>Zirconia, titanium and composite blocks are milled on site with tight tolerances for fit.</p>
      <span class="btn btn-grey">More</span>
    </div>
    <div class="feature">
      <div class="icon"><svg width="20" height="20" viewBox="0 0 20 20"><path d="M4 10l4 4 8-8" fill="none" stroke="#fff" stroke-width="2"/></svg></div>
      <h3>Fast 3D printing</h3>
      <p>Models, guides and temporaries are printed overnight so your chairside schedule stays on track.</p>
      <span class="btn btn-grey">More</span>
    </div>
  </div>
</section>

<section class="step">
  <div class="media photo" role="img" aria-label="Close-up of an open mouth during a dental examination with a mirror"></div>
  <div class="panel"></div>
  <h2>Step by step<br>procedure</h2>
  <p>From scan to final fit, we guide each case through clear and traceable stages.</p>
  <span class="to-top"><svg width="16" height="16" viewBox="0 0 16 16"><path d="M3 10l5-5 5 5" fill="none" stroke="#999" stroke-width="2"/></svg></span>
</section>

<section class="news">
  <div class="wrap">
    <div class="news-list">
      <div class="section-label">Fresh news and events</div>
      <div class="item">
        <div class="date"><b>30</b><span>DEC</span></div>
        <div><h4>New milling centre</h4><p>Our new five axis unit doubles capacity for crowns, bridges and implant abutments now.</p></div>
      </div>
      <div class="item">
        <div class="date"><b>28</b><span>DEC</span></div>
        <div><h4>Open lab day</h4><p>Dentists are invited to tour the lab, meet our technicians and see digital workflows.</p></div>
      </div>
      <div class="item">
        <div class="date"><b>26</b><span>DEC</span></div>
        <div><h4>Student workshop series</h4><p>Dental students can join hands on sessions on scanning, design and finishing of restorations.</p></div>
      </div>
      <span class="btn btn-teal">Read more</span>
    </div>
    <div class="news-side">
      <div class="img img-a" role="img" aria-label="Dentist examining a patient in a bright clinic"></div>
      <h3>Diagnosing unique problems &amp; oral surgery</h3>
      <div class="img img-b" role="img" aria-label="Smiling woman holding a toothbrush"></div>
      <h3>Highest standards of dental treatment</h3>
    </div>
  </div>
</section>

<section class="smile">
  <h2><em>Improving</em> the look of your smile!</h2>
  <svg class="arrow" style="left:360px" width="12" height="20" viewBox="0 0 12 20"><path d="M10 2L2 10l8 8" fill="none" stroke="#bbb" stroke-width="2"/></svg>
  <div class="img" role="img" aria-label="Close-up of a bright white smile"></div>
  <svg class="arrow" style="left:828px" width="12" height="20" viewBox="0 0 12 20"><path d="M2 2l8 8-8 8" fill="none" stroke="#bbb" stroke-width="2"/></svg>
  <p>Natural looking restorations start with careful shade matching and a close dialogue with the practice. We combine handcrafted ceramics with digital precision so each crown, veneer and bridge blends in and lasts for many years.</p>
  <span class="btn btn-teal">Read more</span>
</section>

<section class="advantages">
  <div class="wrap">
    <div class="section-label">Our advantages</div>
    <div class="cols">
      <div class="col"><h3>Easy to remove</h3><p>Removable appliances are designed for easy handling by patients and quick adjustments in clinic.</p><span class="btn btn-outline">Read more</span></div>
      <div class="col"><h3>No drilling</h3><p>Minimal prep veneers and bonded solutions preserve healthy tooth structure wherever it is possible.</p><span class="btn btn-outline">Read more</span></div>
      <div class="col"><h3>Safe &amp; Viable</h3><p>Certified biocompatible materials and documented processes keep every restoration safe and reliable long term.</p><span class="btn btn-outline">Read more</span></div>
    </div>
  </div>
</section>

<section class="banner">
  <div class="media photo" role="img" aria-label="Close-up of teeth with a small decorative gem on a tooth"></div>
  <div class="card">
    <h2>Giving every patient the opportunity to shine</h2>
    <span class="go"><svg width="22" height="22" viewBox="0 0 22 22"><path d="M8 4l7 7-7 7" fill="none" stroke="#ee2848" stroke-width="3"/></svg></span>
  </div>
</section>

<footer class="footer">
  <div class="wrap">
    <small>© 2015 | Privacy Policy</small>
    <div class="social"><span></span><span></span><span></span><span></span><span></span></div>
  </div>
</footer>

</body>
</html>
```